A design led business card for the construction industry

High-end business card to match logo. White logo on dark grey/off black to the front. Matching dark font on white to back, possibly with logo design again.

We offer construction and project management services to commercial and private clients in the UK. Projetcs range from newbuilds, conversion of listed buildings and refurbishments and extensions of existing homes. Our focus is on quality and attention to detail using the highest skills.

Contact Information for Business Card

Name; Dylan Marsh BSc
Position; Project Manager
Mobile; 07961 284 657
Tel; 01632 845192
email; dylan@craftvale.co.uk
web; www.craftvale.co.uk
Address; Kelston on Weald, KT4 7PX

Colors

Designer to choose only greyscale colors for use in the design.

Requirements
Must have
• To include the below description of the business,

CONSTRUCTION - PROJECT MANAGEMENT
Nice to have
• The posibility of the top back of the card being used as a ruler. So will have a measurement to scale in mm or an architect scale of 1:50
Should not have
• Should not be portrait

```html
<!DOCTYPE html>
<html lang="en">
<head>
<meta charset="utf-8">
<title>Craftvale Business Card</title>
<link href="https://fonts.googleapis.com/css2?family=Arimo:wght@400;700&display=swap" rel="stylesheet">
<style>
  :root {
    --backdrop: #e4e4e2;
    --card: #2f2f2f;
    --card-deep: #222222;
    --card-sheen: #3a3a3a;
    --ink: #ffffff;
    --ink-soft: #e6e6e6;
    --rule: #d8d8d8;
  }
  * { box-sizing: border-box; margin: 0; padding: 0; }
  html, body {
    width: 1200px; height: 801px; overflow: hidden;
    background: var(--backdrop);
    font-family: "Arimo", Arial, sans-serif;
  }
  .stage {
    position: relative; width: 1200px; height: 801px;
    display: flex; align-items: center; justify-content: center; gap: 50px;
  }
  .card {
    position: relative; width: 540px; height: 350px;
    background: var(--card); color: var(--ink);
    box-shadow: 0 10px 24px rgba(0,0,0,0.25);
    overflow: hidden;
  }

  /* Front */
  .brand-block {
    position: absolute; left: 40px; top: 0; width: 210px; height: 100%;
    display: flex; flex-direction: column; align-items: center; justify-content: center; gap: 26px;
  }
  .brand-square {
    width: 92px; height: 92px; border: 3px solid var(--ink);
  }
  .brand-name {
    font-size: 17px; font-weight: 400; letter-spacing: 9px; margin-right: -9px;
  }
  .divider {
    position: absolute; left: 270px; top: 55px; width: 1px; height: 240px; background: var(--rule);
  }
  .details {
    position: absolute; left: 298px; top: 58px; width: 230px;
  }
  .person-name { font-size: 21px; font-weight: 700; line-height: 1.1; }
  .person-role { font-size: 13px; color: var(--ink-soft); margin-top: 3px; }
  .address { font-size: 13px; color: var(--ink-soft); line-height: 1.25; margin-top: 20px; }
  .contact-list { list-style: none; margin-top: 20px; }
  .contact-list li {
    display: flex; align-items: center; gap: 8px;
    font-size: 13px; line-height: 1; color: var(--ink-soft); margin-bottom: 5px;
  }
  .contact-list svg { width: 11px; height: 11px; flex: none; }

  /* Back */
  .pattern-field {
    position: absolute; inset: 0;
    background: linear-gradient(100deg, var(--card-deep) 0%, var(--card) 45%, var(--card-sheen) 70%, var(--card) 100%);
  }
  .back-brand {
    position: absolute; left: 190px; top: 138px;
    display: flex; align-items: center; gap: 18px;
  }
  .back-brand .brand-square { width: 70px; height: 70px; }
  .back-text { display: flex; flex-direction: column; }
  .back-text .brand-name { font-size: 19px; letter-spacing: 8px; margin-right: 0; }
  .tagline { font-size: 10px; color: var(--ink-soft); line-height: 1.3; margin-top: 6px; letter-spacing: 0.3px; }
</style>
</head>
<body>
<main class="stage">

  <section class="card card-front">
    <div class="brand-block">
      <div class="brand-square"></div>
      <div class="brand-name">CRAFTVALE</div>
    </div>
    <div class="divider"></div>
    <div class="details">
      <p class="person-name">Dylan Marsh BSc</p>
      <p class="person-role">Project Manager</p>
      <p class="address">Kelston on Weald<br>KT4 7PX</p>
      <ul class="contact-list">
        <li>
          <svg viewBox="0 0 12 12"><rect x="3" y="0.5" width="6" height="11" rx="1" fill="none" stroke="#fff" stroke-width="1"/><circle cx="6" cy="9.6" r="0.6" fill="#fff"/></svg>
          07961 284 657
        </li>
        <li>
          <svg viewBox="0 0 12 12"><path d="M2.5 1.5 L4.5 1 L5.5 3.5 L4.2 4.5 Q5 7 7.5 7.8 L8.5 6.5 L11 7.5 L10.5 9.5 Q5 10 2.5 1.5Z" fill="#fff"/></svg>
          01632 845192
        </li>
        <li>
          <svg viewBox="0 0 12 12"><rect x="0.5" y="2" width="11" height="8" fill="#fff"/><path d="M0.5 2 L6 6.5 L11.5 2" fill="none" stroke="#2f2f2f" stroke-width="1"/></svg>
          dylan@craftvale.co.uk
        </li>
        <li>
          <svg viewBox="0 0 12 12"><circle cx="6" cy="6" r="5.2" fill="none" stroke="#fff" stroke-width="1.2"/><ellipse cx="6" cy="6" rx="2.2" ry="5.2" fill="none" stroke="#fff" stroke-width="1"/><line x1="0.8" y1="6" x2="11.2" y2="6" stroke="#fff" stroke-width="1"/></svg>
          www.craftvale.co.uk
        </li>
      </ul>
    </div>
  </section>

  <section class="card card-back">
    <div class="pattern-field" role="img" aria-label="Embossed repeating tile pattern in dark grey tones"></div>
    <div class="back-brand">
      <div class="brand-square"></div>
      <div class="back-text">
        <span class="brand-name">CRAFTVALE</span>
        <span class="tagline">CONSTRUCTION<br>PROJECT MANAGEMENT</span>
      </div>
    </div>
  </section>

</main>
</body>
</html>
```